KVT website

Im a Specialty contractor that specializes in fireproofing. Epoxy flooring and terrazo along with poured floors and polished concrete.

We also do fire caulking.

Im the largest specialty flooring healthcare contractor in the south east.

Dane

Contractor

```html
<!DOCTYPE html>
<html lang="en">
<head>
<meta charset="utf-8">
<title>KVT — Specialty Flooring &amp; Fireproofing</title>
<link rel="stylesheet" href="https://fonts.googleapis.com/css2?family=Source+Sans+3:wght@400;600&family=Dosis:wght@600;700&display=swap">
<style>
  :root{
    --blue:#27a6df;
    --blue-light:#55bff0;
    --blue-dark:#1894d1;
    --orange:#f7941d;
    --orange-link:#f26522;
    --text:#444;
    --muted:#666;
    --line:#dcdcdc;
    --footer:#f4f4f4;
  }
  *{box-sizing:border-box;margin:0;padding:0}
  html,body{width:932px;height:1200px;overflow:hidden;background:#fff}
  body{position:relative;font-family:"Source Sans 3",Arial,sans-serif;color:var(--text)}
  .abs{position:absolute}
  .top-strip{left:0;top:0;width:932px;height:5px;background:#e6e6e6}
  .utility{right:50px;top:12px;font-size:11px;color:#555}
  .utility span{margin:0 5px;color:#999}
  .brand{left:39px;top:38px;font-size:40px;font-weight:400;color:var(--blue);letter-spacing:1px;line-height:1}
  .slogan{left:42px;top:78px;font-size:12px;color:#555}
  .call{right:51px;top:42px;font-size:19px;color:#444}
  .search{left:649px;top:79px;width:241px;height:29px;border:1px solid #ddd;background:#fff}
  .search .ph{position:absolute;left:9px;top:6px;font-size:11px;color:#888}
  .search .btn{position:absolute;right:0;top:0;width:29px;height:27px;border-left:1px solid #ddd}
  .nav{left:26px;top:122px;width:869px;height:49px;border-radius:3px;
       background:linear-gradient(#5cc3f1,#1d9bd7);display:flex}
  .nav a{flex:1;color:#fff;text-decoration:none;font-size:14px;text-align:center;line-height:49px;
         border-right:1px solid #1787c0;box-shadow:inset -1px 0 0 #6fcaf3}
  .nav a:last-child{border-right:0;box-shadow:none}
  .hero{left:28px;top:177px;width:869px;height:314px;border:1px solid #e3e3e3}
  .hero-photo{position:absolute;left:0;top:0;width:586px;height:312px;
    background:linear-gradient(100deg,#6f8a74 0%,#b8c7b0 35%,#d7d8a0 55%,#c7cfc9 80%,#a8b8ad 100%)}
  .hero-copy{position:absolute;left:610px;top:26px;width:256px}
  .hero-copy h1{font-family:"Dosis",sans-serif;font-weight:700;font-size:21px;line-height:27px;color:var(--blue);
    white-space:nowrap;letter-spacing:-0.2px}
  .hero-copy h1 .alt{color:var(--orange);font-size:18px;letter-spacing:-0.4px}
  .hero-copy p{margin-top:6px;font-size:11px;line-height:16px;color:var(--muted)}
  .checks{list-style:none;margin-top:10px}
  .checks li{font-size:11px;color:var(--muted);height:22px;display:flex;align-items:center;gap:6px}
  .hero-btn{position:absolute;top:250px;height:26px;line-height:26px;color:#fff;font-family:"Dosis",sans-serif;
    font-weight:700;font-size:13px;text-align:center;border-radius:3px}
  .btn-orange{left:614px;width:92px;background:linear-gradient(#ffa936,#f58a0c)}
  .btn-blue{left:717px;width:86px;background:linear-gradient(#5cc3f1,#1d9bd7)}
  .card{top:515px;width:270px;height:244px;border:1px solid #dedede;border-radius:0 0 4px 4px}
  .card .photo{height:124px}
  .card h3{margin:15px 0 0 14px;font-size:15px;font-weight:400;color:#333}
  .card p{margin:6px 12px 0 14px;font-size:10px;line-height:16px;color:var(--muted)}
  .more{font-size:11px;color:var(--orange-link);display:inline-flex;align-items:center;gap:4px}
  .card .more{position:absolute;left:15px;top:215px}
  .tri{width:0;height:0;border-left:4px solid var(--orange-link);border-top:3.5px solid transparent;border-bottom:3.5px solid transparent}
  .rule{left:34px;top:786px;width:852px;border-top:1px dotted #bbb}
  .section-title{font-size:15px;color:#333;font-weight:400}
  .project{top:841px;width:184px}
  .project .photo{height:111px}
  .project h4{margin-top:12px;font-size:12px;font-weight:400;color:#444;padding-left:4px}
  .project p{margin-top:6px;font-size:10px;line-height:16px;color:var(--muted);padding-left:4px}
  .small-btn{position:absolute;top:234px;left:3px;width:70px;height:23px;line-height:23px;border-radius:3px;
    background:linear-gradient(#4bb9ec,#1d9bd7);color:#fff;font-size:10.5px;text-align:center}
  .vdivider{left:631px;top:820px;height:275px;border-left:1px solid #e6e6e6}
  .news{left:648px;width:250px}
  .news h5{font-size:12.5px;font-weight:400;color:var(--blue)}
  .news p{margin-top:3px;font-size:10px;line-height:16px;color:var(--muted)}
  .view-more{left:648px;top:1091px;height:23px;padding:0 8px;background:#f6f6f6;border-radius:2px}
  .footer{left:0;top:1133px;width:932px;height:50px;background:var(--footer)}
  .footer .copy{position:absolute;left:36px;top:17px;font-size:10px;color:#777}
  .footer .links{position:absolute;right:36px;top:17px;font-size:10.5px;color:#555}
  .footer span.sep{margin:0 6px;color:#999}
</style>
</head>
<body>
  <div class="abs top-strip"></div>

  <header>
    <div class="abs utility">FAQ<span>|</span>Support<span>|</span>Members<span>|</span>Partners<span>|</span>Sitemap</div>
    <div class="abs brand">KVT</div>
    <div class="abs slogan">your slogan goes here</div>
    <div class="abs call">Call Us +696-555-0142</div>
    <div class="abs search">
      <span class="ph">Enter keyword</span>
      <span class="btn">
        <svg width="29" height="27" viewBox="0 0 29 27"><circle cx="14" cy="12.5" r="5" fill="none" stroke="#27a6df" stroke-width="2"/><line x1="17.5" y1="16" x2="21" y2="19.5" stroke="#27a6df" stroke-width="2.4" stroke-linecap="round"/></svg>
      </span>
    </div>
    <nav class="abs nav">
      <a>Company</a><a>Our Services</a><a>Our Projects</a><a>Recent News</a><a>Testimonials</a><a>Recent Blog</a><a>Contact Us</a>
    </nav>
  </header>

  <section class="abs hero">
    <div class="hero-photo" role="img" aria-label="Photo of two contractors in hard hats and safety vests reviewing plans on site"></div>
    <div class="hero-copy">
      <h1>We Are Contractors for<br><span class="alt">Fireproofing Floors &amp; Buildings</span></h1>
      <p>Lorem ipsum dolor sit amet, consectetuer adipiscing elit. Nam cursus. Morbi ut mi. Nullam enim leo, egestas id, condimentum at.</p>
      <ul class="checks">
        <li><svg width="11" height="9" viewBox="0 0 11 9"><path d="M1 4.5l3 3 6-6" fill="none" stroke="#999" stroke-width="2"/></svg>Pellentesque habitant morbi</li>
        <li><svg width="11" height="9" viewBox="0 0 11 9"><path d="M1 4.5l3 3 6-6" fill="none" stroke="#999" stroke-width="2"/></svg>Tristique senectus et netus et</li>
        <li><svg width="11" height="9" viewBox="0 0 11 9"><path d="M1 4.5l3 3 6-6" fill="none" stroke="#999" stroke-width="2"/></svg>Malesuada fames ac turpis egestas.</li>
        <li><svg width="11" height="9" viewBox="0 0 11 9"><path d="M1 4.5l3 3 6-6" fill="none" stroke="#999" stroke-width="2"/></svg>In posuere felis nec tortor.</li>
      </ul>
    </div>
    <div class="hero-btn btn-orange">VIEW PROJECT</div>
    <div class="hero-btn btn-blue">READ MORE</div>
  </section>

  <section>
    <article class="abs card" style="left:29px">
      <div class="photo" role="img" aria-label="Photo of a worker applying epoxy floor coating" style="background:linear-gradient(120deg,#b88a6e,#c9cdd0 45%,#a9b2b8)"></div>
      <h3>Epoxy Flooring</h3>
      <p>Lorem ipsum dolor sit amet, consectetuer adipiscing elit. Nam cursus. Morbi ut mi. Nullam enim leo, egestas id, condimentum at, laoreet mattis, massa.</p>
      <span class="more">LEARN MORE <i class="tri"></i></span>
    </article>
    <article class="abs card" style="left:324px">
      <div class="photo" role="img" aria-label="Photo of terrazzo steps and walkway with plants" style="background:linear-gradient(160deg,#7d8f6a,#c8b8a6 40%,#d9cdbf 70%,#8fa06e)"></div>
      <h3>Terrazo</h3>
      <p>Lorem ipsum dolor sit amet, consectetuer adipiscing elit. Nam cursus. Morbi ut mi. Nullam enim leo, egestas id, condimentum at</p>
      <span class="more">LEARN MORE <i class="tri"></i></span>
    </article>
    <article class="abs card" style="left:620px">
      <div class="photo" role="img" aria-label="Photo of a compact loader on a concrete yard" style="background:linear-gradient(170deg,#8a9688,#9aa2a4 45%,#c6a23a 60%,#9ea3a6)"></div>
      <h3>Polishing Concrete</h3>
      <p>Lorem ipsum dolor sit amet, consectetuer adipiscing elit. Nam cursus. Morbi ut mi. Nullam enim leo, egestas id, condimentum at</p>
      <span class="more">LEARN MORE <i class="tri"></i></span>
    </article>
  </section>

  <div class="abs rule"></div>

  <section>
    <h2 class="abs section-title" style="left:35px;top:811px">Recent Projects</h2>
    <article class="abs project" style="left:34px">
      <div class="photo" role="img" aria-label="Photo of a warehouse floor with a roller conveyor" style="background:linear-gradient(135deg,#8fa3ad,#c6cacb 50%,#9ab0bb)"></div>
      <h4>Project Name</h4>
      <p>Proin dui lectus, cursus eu, mattis laoreet, viverra sit amet, quam. Curabitur vel dolor ultrices ipsum dictum tristique. Praesent vitae lacus. Ut velit enim, vestibulum non</p>
      <span class="small-btn">Learn more</span>
    </article>
    <article class="abs project" style="left:232px">
      <div class="photo" role="img" aria-label="Photo of floor grinding machines in a workshop" style="background:linear-gradient(135deg,#d7d7d3,#6e7072 50%,#c5c5c0)"></div>
      <h4>Project Name</h4>
      <p>Proin dui lectus, cursus eu, mattis laoreet, viverra sit amet, quam. Curabitur vel dolor ultrices ipsum dictum tristique. Praesent vitae lacus. Ut velit enim, vestibulum non</p>
      <span class="small-btn">Learn more</span>
    </article>
    <article class="abs project" style="left:431px">
      <div class="photo" role="img" aria-label="Photo of a furnished lounge with a finished wooden floor" style="background:linear-gradient(160deg,#ede9e1,#e6dccb 50%,#b07a45)"></div>
      <h4>Project Name</h4>
      <p>Proin dui lectus, cursus eu, mattis laoreet, viverra sit amet, quam. Curabitur vel dolor ultrices ipsum dictum tristique. Praesent vitae lacus. Ut velit enim, vestibulum non</p>
      <span class="small-btn">Learn more</span>
    </article>
  </section>

  <div class="abs vdivider"></div>

  <aside>
    <h2 class="abs section-title" style="left:648px;top:811px">Latest News &amp; Blog</h2>
    <div class="abs news" style="top:840px">
      <h5>Proin dui lectus, cursus eu</h5>
      <p>Mattis laoreet, viverra sit amet, quam. Curabitur vel dolor ultrices ipsum dictum tristique.</p>
    </div>
    <div class="abs news" style="top:903px">
      <h5>Nunc tempus felis vitae urna</h5>
      <p>Duis non nunc. Nulla rhoncus dictum metus. Curabitur tristique mi condimentum orci. Phasellus pellentesque aliquam enim</p>
    </div>
    <div class="abs news" style="top:982px">
      <h5>Phasellus felis dolor</h5>
      <p>Phasellus felis dolor, scelerisque a, tempus eget, lobortis id, libero. Phasellus felis dolor, scelerisque a, tempus eget, lobortis id, libero. Donec scelerisque leo ac risus. Praesent sit amet est. In dictum, dolor eu dictum porttitor, enim felis viverra mi.</p>
    </div>
    <span class="abs more view-more">VIEW MORE <i class="tri"></i></span>
  </aside>

  <footer class="abs footer">
    <div class="copy">© 2012 Company Name <span class="sep">|</span>Term of Use<span class="sep">|</span>Privacy Policy</div>
    <div class="links">Company<span class="sep">|</span>Our Services<span class="sep">|</span>Our Projects<span class="sep">|</span>Recent News<span class="sep">|</span>Testimonials<span class="sep">|</span>Recent Blog<span class="sep">|</span>Contact Us</div>
  </footer>
</body>
</html>
```